Create a beautiful brochure for a Permanent Make Up Clinic

I need a classy brochure for my Permanent Make up Clinic. It needs a classy cover and the list of services and extra information on the inside. I don't have any requirements on size of the brochure, but it needs to look attractive and upmarket. The colors I like are black -white - Gold - grey. I like a minimalistic look.
I’d like to have my logo on the cover, the price list on the inside and the address information at the back.

Target Market(s)

woman between 18 and 99 years old

Industry/Entity Type

Beauty

Font styles to use
Sans Serif
Script

Colors

Designer to choose colors to be used in the design.

Requirements
Must have
• the logo on the cover
• pictures of the services with an explanation and pricing
• address information at the back
Nice to have
• a classy upmarket look, not with too many different colors in it.

```html
<!DOCTYPE html>
<html lang="nl">
<head>
<meta charset="utf-8">
<title>Lumé Clinic – Brochure</title>
<link href="https://fonts.googleapis.com/css2?family=Montserrat:wght@300;400;600&family=Great+Vibes&display=swap" rel="stylesheet">
<style>
:root{
  --bg:#e8e8e9;
  --paper:#ffffff;
  --grey:#5e5e62;
  --grey-dark:#4d4d51;
  --rose:#d2a392;
  --rose-soft:#e9cfc4;
  --text:#6b6b6f;
  --light:#f3f3f3;
}
*{margin:0;padding:0;box-sizing:border-box}
html,body{width:845px;height:1200px;overflow:hidden;background:var(--bg);font-family:'Montserrat',sans-serif;color:var(--text)}
.sheet{position:absolute;left:20px;width:805px;height:545px;display:flex;box-shadow:0 4px 14px rgba(0,0,0,.18)}
.sheet--outside{top:22px}
.sheet--inside{top:628px}
.panel{position:relative;width:268.33px;height:100%;background:var(--paper);overflow:hidden}
.panel+.panel{border-left:1px solid rgba(0,0,0,.06)}
.panel--grey{background:var(--grey);color:#e4e4e4}
.photo{position:absolute;left:0;width:100%}
.small{font-size:6.3px;line-height:1.55}
.rose{color:var(--rose)}
.caps{text-transform:uppercase;letter-spacing:1.4px}
.script{font-family:'Great Vibes',cursive;color:var(--rose)}
.web{position:absolute;bottom:14px;width:100%;text-align:center;font-size:7px;letter-spacing:1.5px;color:var(--rose)}
.brand{font-family:'Montserrat',sans-serif;font-weight:300;color:var(--grey);letter-spacing:4px;display:flex;align-items:center;gap:8px}
.brand-dot{width:9px;height:9px;border-radius:50%;background:var(--rose)}
/* outside left */
.intro{position:absolute;top:18px;left:18px;right:18px;color:var(--rose)}
.offer{position:absolute;top:62px;left:18px;right:18px}
.offer h3{font-size:9px;font-weight:600;color:var(--rose);letter-spacing:1px;border-top:1px solid var(--rose-soft);border-bottom:1px solid var(--rose-soft);padding:5px 0;margin-bottom:8px}
.offer-row{display:flex;gap:10px;align-items:center;margin:10px 0}
.circle{flex:none;border-radius:50%}
/* outside middle */
.contact-brand{position:absolute;top:48px;width:100%;justify-content:center;font-size:20px}
.contact-portrait{position:absolute;top:100px;left:84px;width:100px;height:100px;border:3px solid var(--rose-soft)}
.contact-copy{position:absolute;top:214px;left:26px;right:26px;text-align:center}
.contact-copy h4{font-size:8px;font-weight:600;margin:10px 0 3px;color:var(--rose);letter-spacing:1.5px}
.contact-band{position:absolute;left:0;right:0;top:380px;bottom:0;background:var(--grey);color:#e9e9e9;text-align:center;padding-top:22px}
.socials{display:flex;justify-content:center;gap:12px;margin:12px 0;font-size:6px;align-items:center}
.socials span{display:inline-flex;align-items:center;gap:4px}
.socials i{width:9px;height:9px;border-radius:50%;background:var(--rose);display:inline-block}
/* outside right (cover) */
.cover-brand{position:absolute;top:34px;right:22px;font-size:22px}
.cover-band{position:absolute;top:308px;left:0;right:0;height:86px;background:var(--grey);text-align:center;padding-top:22px}
.cover-band h1{font-size:13px;font-weight:300;letter-spacing:3px;color:#fff}
.cover-band p{font-size:15px;margin-top:4px}
/* inside */
.motto{position:absolute;top:22px;left:20px;right:20px}
.motto h2{font-family:'Great Vibes',cursive;font-weight:400;font-size:20px;line-height:1;color:var(--rose);margin-bottom:12px}
.motto h5{font-size:7px;color:var(--rose);font-weight:600;margin:12px 0 6px}
.motto ol{padding-left:10px}
.motto li{margin-bottom:3px}
.service{position:absolute;left:20px;right:20px}
.service h4{font-size:7.5px;font-weight:600;letter-spacing:1px;display:flex;justify-content:space-between;color:var(--rose);margin-bottom:4px}
.lip-band{position:absolute;left:0;right:0;top:400px;bottom:0;background:var(--grey);color:#e4e4e4}
.price-list{position:absolute;top:214px;left:20px;right:20px}
.price-item{margin-bottom:13px}
.price-item h4{font-size:7px;font-weight:600;letter-spacing:1px;color:var(--rose);display:flex;justify-content:space-between;margin-bottom:3px}
</style>
</head>
<body>

<!-- Outside spread -->
<section class="sheet sheet--outside">
  <article class="panel">
    <p class="intro small">Bij Lumé Clinic staan jouw wensen centraal. Wij werken met zorg, rust en aandacht voor elk detail van jouw gezicht.</p>
    <div class="offer">
      <h3>GRATIS ADVIESGESPREK</h3>
      <p class="small">Tijdens een vrijblijvend gesprek bekijken we samen welke behandeling het best past bij jouw gelaat, huidtype en persoonlijke stijl. Zo weet je vooraf precies wat je mag verwachten.</p>
      <div class="offer-row">
        <div class="circle" role="img" aria-label="Round portrait of a client" style="width:70px;height:70px;background:radial-gradient(circle at 45% 40%,#e8d2c6,#9c8a82)"></div>
        <p class="small">Elke behandeling start met een zorgvuldige voortekening op maat.</p>
      </div>
      <p class="small">Na de behandeling krijg je een nazorgset en een gratis controle na zes weken.</p>
    </div>
    <div class="photo" role="img" aria-label="Photo of a brow treatment in progress" style="top:370px;height:175px;background:linear-gradient(135deg,#8d8a8a,#d9d2cf 55%,#6f6c6d)"></div>
  </article>

  <article class="panel">
    <div class="brand contact-brand"><span class="brand-dot"></span>LUMÉ CLINIC</div>
    <div class="circle contact-portrait" role="img" aria-label="Round portrait of a woman with natural make-up" style="background:radial-gradient(circle at 50% 40%,#f0ddd2,#b79b8e)"></div>
    <div class="contact-copy">
      <p class="small">Geen idee welke behandeling bij jou past? Neem gerust contact op, wij helpen je graag verder met persoonlijk advies.</p>
      <h4>HEB JE NOG VRAGEN?</h4>
      <p class="small">Bel/Whatsapp +32 470 12 34 56</p>
    </div>
    <div class="contact-band">
      <p class="small" style="font-weight:600">Vind ons afspraak</p>
      <p class="small">Lumé Clinic<br>Lindenlaan 12<br>9000 Gent</p>
      <div class="socials"><span><i></i>@lumeclinic</span><span><i></i>@lumeclinic</span></div>
      <p class="web" style="bottom:16px">www.lumestudio.be</p>
    </div>
  </article>

  <article class="panel">
    <div class="photo" role="img" aria-label="Close-up photo of a woman's face with soft make-up" style="top:0;height:308px;background:linear-gradient(120deg,#f6f1ee 35%,#e6cfc3 65%,#c9aa9b)"></div>
    <div class="brand cover-brand"><span class="brand-dot"></span>LUMÉ CLINIC</div>
    <div class="cover-band">
      <h1>PERMANENT MAKE UP</h1>
      <p class="script">Eenvoud is natuurlijke schoonheid</p>
    </div>
    <p class="web">www.lumeclinic.be</p>
  </article>
</section>

<!-- Inside spread -->
<section class="sheet sheet--inside">
  <article class="panel panel--grey">
    <div class="motto">
      <h2>Eenvoud is natuurlijke schoonheid</h2>
      <p class="small">Permanent make-up accentueert je natuurlijke trekken. Je bent elke ochtend klaar, zonder gedoe, en je ziet er altijd verzorgd uit. Bij Lumé Clinic werken we met hoogwaardige pigmenten en de nieuwste technieken voor een zacht resultaat.</p>
      <h5>Waarom kiezen voor permanente make-up?</h5>
      <ol class="small">
        <li>Je bespaart elke dag tijd bij het opmaken.</li>
        <li>Het resultaat is waterbestendig en blijft mooi.</li>
        <li>Ideaal bij allergieën voor gewone make-up.</li>
        <li>Een natuurlijk effect dat bij jou past.</li>
        <li>Persoonlijke begeleiding van begin tot eind.</li>
      </ol>
    </div>
    <p class="web">www.lumestudio.be</p>
  </article>

  <article class="panel">
    <div class="service" style="top:22px">
      <p class="small">Het concept van Lumé Clinic is fundamenteel anders. Wij combineren vakmanschap met een persoonlijke aanpak zodat elk resultaat perfect aansluit bij jouw gezicht.</p>
    </div>
    <div class="service" style="top:84px">
      <h4><span>POWDER BROWS</span><span>€350</span></h4>
      <p class="small">Een zachte poedertechniek die volle, gedefinieerde wenkbrauwen geeft. Ideaal voor wie een opgemaakt maar natuurlijk effect wenst dat lang meegaat.</p>
    </div>
    <div class="photo" role="img" aria-label="Photo of eyebrows being treated" style="top:160px;height:140px;background:linear-gradient(135deg,#b7aaa5,#ece4e0 50%,#8f8482)"></div>
    <div class="service" style="top:312px">
      <p class="small">Inclusief voortekening, behandeling en controle. De kleur wordt afgestemd op jouw haar en huidtint.</p>
    </div>
    <div class="lip-band">
      <div class="service" style="top:22px">
        <h4><span>FULL LIP / LIP BLUSH TECHNIEK</span><span>€380</span></h4>
        <p class="small">Deze techniek zorgt voor een frisse kleur en een mooie lipcontour. Je lippen lijken voller en krijgen een zachte blos die natuurlijk oogt. Na genezing blijft de kleur subtiel en egaal aanwezig.</p>
      </div>
    </div>
  </article>

  <article class="panel panel--grey">
    <div class="photo" role="img" aria-label="Close-up photo of an eye with eyeliner and lashes" style="top:0;height:200px;background:linear-gradient(110deg,#f4ede9,#d9c4b9 60%,#a58f85)"></div>
    <div class="price-list">
      <div class="price-item"><h4><span>OGENLIJNTJE</span><span>€250</span></h4><p class="small">Een fijne lijn tussen de wimpers die je blik opent en versterkt.</p></div>
      <div class="price-item"><h4><span>EYELINER</span><span>€300</span></h4><p class="small">Een duidelijke lijn die je ogen elke dag mooi omlijnt.</p></div>
      <div class="price-item"><h4><span>LIP CONTOUR</span><span>€280</span></h4><p class="small">Een strakke omlijning voor meer vorm en symmetrie.</p></div>
      <div class="price-item"><h4><span>BIJWERKING</span><span>€120</span></h4><p class="small">Opfrissing van een eerdere behandeling binnen twee jaar.</p></div>
    </div>
    <p class="web">www.lumestudio.be</p>
  </article>
</section>

</body>
</html>
```